Van Signage Wrapping

Hi there, my name is Wade; I have a business called "Vorplex" servicing the Electrical, Security & AV (audio visual) industry. I currently have 2 X Vans working in Australia; I am looking to design a the graphics & lay out for the 2 X vans to be identical wrapped.
Should you wish to see the Van appearance (silver)
http://www.morvane.com.au/cars/kelsovan/colours
http://www.morvane.com.au/cars/kelsovan/home

Dimensions of the side panels are:
from the revision mirror to the tail 3.6meters
from the bottom if plastic to the top 1.35meters

Some of the words that describe our services are:
Commercial, Domestic, Automation, Networking, Data, Access Control, Alarms, CCTV, Audio Visual, Surround Sound, Home Cinema.
Allot of our work is taking these various technologies & linking them together for the user
Updates

Hi there, I have added a couple of thoughts in the 'nice to have' area of the brief I am very interested to see how you guys go, thank you for your designs so farĀ 

Target Market(s)

Builders, Developers, Home Owners, Buissness Owners

Industry/Entity Type

Plastic

Requirements
Must have
• The Logo "Vorplex" which is attached to the project
(m)0412 557 163
(e)sales@vorplex.com.au

I would like the side Logo on the van to run diagonal & hopefully take most of the advertising space over the sliding door & rear panel

REC No: 48302
Nice to have
• I have spent a little extra money on the Vans with more to come and I believe they look sharp & clean with the view to target well to do clients & larger projects, it would be great to keep the vans looking professional & clean. I like blue, white, black, lime-pale green against the silver colour but open to surjection.
In my head I imagined the Vorplex logo running on the largest side panels on the diagonal with the Electrical, Security, AV also running the length underneath the logo. With some of the words mentioned above that describe our services in various shades randomly placed horizontally in the back ground linked together with a sort of printed circuit board pattern. Again I am very open to ideas so please feel free to get creative. You can see one image I have uploaded a picture of a Ute with some words that are randomly placed & similar to the shade I am thinking of, I also like the Lime/Pale Green on the Ute if you can make it work
Measurements of Van Panels are attached

```html
<!DOCTYPE html>
<html lang="en">
<head>
<meta charset="utf-8">
<title>Vorplex Van Wrap Layout</title>
<link href="https://fonts.googleapis.com/css2?family=Arimo:wght@400;700&display=swap" rel="stylesheet">
<style>
  :root{
    --backdrop:#3b2219;
    --body-grey:#7a7a7a;
    --trim-grey:#5e5e5e;
    --tyre:#111111;
    --glass:#ffffff;
    --silver-light:#f2f2f2;
    --silver-mid:#c9c9c9;
    --silver-dark:#9d9d9d;
    --lime:#9ccd2a;
    --green:#3fae3f;
    --blue:#1f6fc4;
    --ink:#2b2b2b;
    --logo:#4a4a4a;
    --light-red:#e0242a;
    --plate-yellow:#f3ea1c;
    --indicator:#f08a1c;
  }
  html,body{margin:0;padding:0;width:1200px;height:677px;overflow:hidden;background:var(--backdrop);}
  .layout{display:block;width:1200px;height:677px;}
  .service{font-family:"Arimo",Arial,sans-serif;font-weight:400;fill:var(--ink);}
  .contact{font-family:"Arimo",Arial,sans-serif;font-weight:700;fill:#ffffff;}
  .licence{font-family:"Arimo",Arial,sans-serif;font-weight:700;fill:var(--ink);}
  .brand-name{font-family:"Arimo",Arial,sans-serif;font-weight:400;fill:var(--logo);}
  .brand-tag{font-family:"Arimo",Arial,sans-serif;font-weight:400;fill:var(--logo);}
  .trim{fill:var(--body-grey);}
  .trim-dark{fill:var(--trim-grey);}
  .tyre{fill:var(--tyre);}
  .glass{fill:var(--glass);}
  .rim{fill:#d9d9d9;stroke:#888;stroke-width:3;}
  .hub{fill:#6d6d6d;}
  .tail-light{fill:var(--light-red);}
  .lamp{fill:#ffffff;}
</style>
</head>
<body>
<svg class="layout" viewBox="0 0 1500 846" xmlns="http://www.w3.org/2000/svg">
  <defs>
    <linearGradient id="wrapSilver" x1="0" y1="0" x2="1" y2="1">
      <stop offset="0" stop-color="var(--silver-mid)"/>
      <stop offset="0.45" stop-color="var(--silver-light)"/>
      <stop offset="1" stop-color="var(--silver-dark)"/>
    </linearGradient>
    <linearGradient id="limeSweep" x1="0" y1="0" x2="1" y2="0">
      <stop offset="0" stop-color="var(--green)"/>
      <stop offset="1" stop-color="var(--lime)"/>
    </linearGradient>

    <g id="sideVan">
      <path class="trim" d="M528,330 L524,270 Q532,232 600,210 L720,62 Q742,32 825,28 L1440,26 Q1462,28 1466,60 L1482,300 L1486,335 L528,335 Z"/>
      <path fill="url(#wrapSilver)" role="img" aria-label="Silver wrap with faint printed circuit board pattern"
            d="M536,296 L536,268 Q546,238 606,218 L724,68 Q746,40 826,36 L1436,34 Q1452,36 1456,62 L1470,296 Z"/>
      <rect class="trim" x="528" y="292" width="958" height="40"/>
      <path class="glass" d="M752,64 L904,50 Q926,50 924,82 L916,165 L800,168 L748,150 Z"/>
      <path fill="var(--blue)" d="M752,150 Q820,190 920,160 L918,178 Q830,200 752,150 Z"/>
      <path fill="url(#limeSweep)" d="M760,148 Q830,182 918,150 L916,166 Q830,190 760,148 Z"/>
      <path fill="var(--blue)" d="M604,236 Q680,190 745,230 L752,272 Q700,222 604,236 Z"/>
      <path fill="url(#limeSweep)" d="M604,232 Q672,188 742,222 L744,258 Q690,214 604,232 Z"/>
      <path fill="var(--blue)" d="M1210,30 L1425,28 L1425,50 Q1310,50 1240,46 Z"/>
      <path fill="url(#limeSweep)" d="M1206,28 L1425,26 L1425,44 Q1300,44 1236,40 Z"/>
      <path fill="var(--blue)" d="M982,178 L1432,178 L1424,222 Q1200,236 1040,236 Q990,230 982,178 Z"/>
      <path fill="url(#limeSweep)" d="M982,174 L1432,174 L1426,212 Q1200,226 1040,226 Q994,220 982,174 Z"/>
      <rect class="trim-dark" x="1168" y="168" width="210" height="12" rx="6"/>
      <rect class="trim-dark" x="908" y="160" width="16" height="44" rx="8"/>
      <rect class="trim-dark" x="954" y="160" width="16" height="44" rx="8"/>
      <rect fill="var(--indicator)" x="680" y="188" width="14" height="8" rx="2"/>
      <path class="lamp" d="M538,246 Q550,222 582,216 L572,252 Z"/>
      <path class="tail-light" d="M1455,105 L1468,105 L1472,200 L1458,200 Z"/>
      <rect class="lamp" x="1454" y="78" width="12" height="14"/>
      <rect class="lamp" x="1460" y="208" width="12" height="14"/>
      <path class="trim-dark" d="M610,335 A72,72 0 0 1 754,335 Z"/>
      <path class="trim-dark" d="M1255,335 A72,72 0 0 1 1400,335 Z"/>
      <circle class="tyre" cx="682" cy="328" r="60"/>
      <circle class="rim" cx="682" cy="328" r="38"/>
      <circle class="hub" cx="682" cy="328" r="12"/>
      <circle class="tyre" cx="1328" cy="328" r="60"/>
      <circle class="rim" cx="1328" cy="328" r="38"/>
      <circle class="hub" cx="1328" cy="328" r="12"/>
    </g>
  </defs>

  <!-- FRONT VIEW -->
  <g class="front-view">
    <rect class="tyre" x="52" y="320" width="44" height="72" rx="8"/>
    <rect class="tyre" x="352" y="320" width="44" height="72" rx="8"/>
    <path class="trim" d="M20,120 Q26,112 50,118 L60,40 Q70,28 90,28 L360,28 Q380,28 390,40 L400,118 Q424,112 428,128 L424,170 L400,180 L406,300 Q406,340 380,340 L70,340 Q44,340 44,300 L50,180 L24,170 Z"/>
    <path fill="url(#wrapSilver)" role="img" aria-label="Silver wrap with faint printed circuit board pattern" d="M66,150 L384,150 L392,236 L58,236 Z"/>
    <path class="glass" d="M78,36 L372,36 Q380,38 378,60 L372,140 L78,140 L72,60 Q72,38 78,36 Z"/>
    <path fill="var(--blue)" d="M78,180 Q100,160 140,170 L138,232 Q110,190 78,180 Z"/>
    <path fill="url(#limeSweep)" d="M80,176 Q104,158 136,166 L134,210 Q110,180 80,176 Z"/>
    <path fill="var(--blue)" d="M372,180 Q350,160 310,170 L312,232 Q340,190 372,180 Z"/>
    <path fill="url(#limeSweep)" d="M370,176 Q346,158 314,166 L316,210 Q340,180 370,176 Z"/>
    <ellipse class="lamp" cx="106" cy="206" rx="34" ry="26"/>
    <ellipse class="lamp" cx="344" cy="206" rx="34" ry="26"/>
    <path fill="var(--indicator)" d="M80,226 L140,236 L138,240 L80,232 Z"/>
    <path fill="var(--indicator)" d="M370,226 L310,236 L312,240 L370,232 Z"/>
    <rect class="trim-dark" x="238" y="158" width="72" height="10" rx="3"/>
    <text class="brand-name" x="161" y="202" font-size="30" textLength="108" lengthAdjust="spacingAndGlyphs">Vorplex</text>
    <text class="brand-tag" x="174" y="210" font-size="5" textLength="62" lengthAdjust="spacingAndGlyphs">ELECTRICAL, SECURITY, AV</text>
    <rect class="trim-dark" x="215" y="222" width="14" height="18" rx="2"/>
    <rect class="trim-dark" x="80" y="262" width="290" height="12" rx="4"/>
    <rect class="glass" x="176" y="280" width="96" height="20"/>
    <rect class="trim-dark" x="150" y="305" width="150" height="28" rx="4"/>
    <circle class="lamp" cx="104" cy="318" r="10"/>
    <circle class="lamp" cx="342" cy="318" r="10"/>
  </g>

  <!-- TOP SIDE VIEW -->
  <use href="#sideVan"/>
  <g class="side-copy">
    <text class="service" font-size="18" transform="translate(940,130) rotate(-26)">Commercial, Domestic</text>
    <text class="service" font-size="18" transform="translate(978,153) rotate(-26)">Automation</text>
    <text class="service" font-size="18" transform="translate(1086,108) rotate(-26)">Networking</text>
    <text class="service" font-size="18" transform="translate(1038,157) rotate(-26)">Data</text>
    <text class="service" font-size="18" transform="translate(1158,126) rotate(-26)">Access Control</text>
    <text class="service" font-size="18" transform="translate(1094,162) rotate(-26)">Alarms</text>
    <text class="service" font-size="18" transform="translate(1180,157) rotate(-26)">Audio Visual</text>
    <text class="service" font-size="18" transform="translate(1290,86) rotate(-26)">CCTV</text>
    <text class="service" font-size="18" transform="translate(1296,120) rotate(-26)">Surround Sound</text>
    <text class="service" font-size="18" transform="translate(1310,158) rotate(-26)">Home Cinema</text>
    <text class="contact" x="1032" y="202" font-size="17">(m)0412 557 163</text>
    <text class="contact" x="1204" y="202" font-size="17">(e)sales@vorplex.com.au</text>
    <text class="licence" x="1074" y="274" font-size="19">REC No: 48302</text>
    <text class="brand-name" x="756" y="272" font-size="62" textLength="195" lengthAdjust="spacingAndGlyphs">Vorplex</text>
    <text class="brand-tag" x="756" y="286" font-size="8" textLength="134" lengthAdjust="spacingAndGlyphs">ELECTRICAL, SECURITY, AV</text>
  </g>

  <!-- BOTTOM SIDE VIEW -->
  <use href="#sideVan" transform="translate(2010,435) scale(-1,1)"/>
  <g class="side-copy">
    <text class="service" font-size="18" transform="translate(580,582) rotate(-26)">Commercial, Domestic</text>
    <text class="service" font-size="18" transform="translate(640,586) rotate(-26)">Automation</text>
    <text class="service" font-size="18" transform="translate(748,540) rotate(-26)">Networking</text>
    <text class="service" font-size="18" transform="translate(700,589) rotate(-26)">Data</text>
    <text class="service" font-size="18" transform="translate(818,556) rotate(-26)">Access Control</text>
    <text class="service" font-size="18" transform="translate(756,594) rotate(-26)">Alarms</text>
    <text class="service" font-size="18" transform="translate(830,592) rotate(-26)">Audio Visual</text>
    <text class="service" font-size="18" transform="translate(950,516) rotate(-26)">CCTV</text>
    <text class="service" font-size="18" transform="translate(946,560) rotate(-26)">Surround Sound</text>
    <text class="service" font-size="18" transform="translate(968,597) rotate(-26)">Home Cinema</text>
    <text class="contact" x="600" y="637" font-size="18">(e)sales@vorplex.com.au</text>
    <text class="contact" x="840" y="637" font-size="18">(m)0412 557 163</text>
    <text class="licence" x="780" y="708" font-size="20">REC No: 48302</text>
    <text class="brand-name" x="1055" y="704" font-size="64" textLength="200" lengthAdjust="spacingAndGlyphs">Vorplex</text>
    <text class="brand-tag" x="1082" y="718" font-size="8" textLength="112" lengthAdjust="spacingAndGlyphs">ELECTRICAL, SECURITY, AV</text>
  </g>

  <!-- REAR VIEW -->
  <g class="rear-view">
    <rect class="tyre" x="52" y="760" width="44" height="66" rx="8"/>
    <rect class="tyre" x="352" y="760" width="44" height="66" rx="8"/>
    <path class="trim" d="M22,570 Q30,556 50,560 L56,472 Q60,460 78,460 L372,460 Q390,460 394,472 L400,560 Q420,556 428,570 L424,604 L400,610 L402,760 L48,760 L50,610 L26,604 Z"/>
    <path fill="url(#wrapSilver)" role="img" aria-label="Silver wrap with faint printed circuit board pattern" d="M78,466 L372,466 L372,740 L78,740 Z"/>
    <rect class="tail-light" x="56" y="532" width="18" height="102" rx="4"/>
    <rect class="tail-light" x="376" y="532" width="18" height="102" rx="4"/>
    <rect class="lamp" x="54" y="510" width="22" height="14"/>
    <rect class="lamp" x="374" y="510" width="22" height="14"/>
    <rect class="tail-light" x="62" y="688" width="12" height="30"/>
    <rect class="tail-light" x="376" y="688" width="12" height="30"/>
    <rect class="tail-light" x="186" y="464" width="28" height="10" rx="2"/>
    <text class="service" font-size="11" transform="translate(86,542) rotate(-26)">Commercial, Domestic</text>
    <text class="service" font-size="11" transform="translate(110,557) rotate(-26)">Automation</text>
    <text class="service" font-size="11" transform="translate(186,521) rotate(-26)">Networking</text>
    <text class="service" font-size="11" transform="translate(178,546) rotate(-26)">Data</text>
    <text class="service" font-size="11" transform="translate(236,526) rotate(-26)">Access Control</text>
    <text class="service" font-size="11" transform="translate(174,570) rotate(-26)">Alarms</text>
    <text class="service" font-size="11" transform="translate(220,562) rotate(-26)">Audio Visual</text>
    <text class="service" font-size="11" transform="translate(304,514) rotate(-26)">CCTV</text>
    <text class="service" font-size="11" transform="translate(284,552) rotate(-26)">Surround Sound</text>
    <text class="service" font-size="11" transform="translate(290,578) rotate(-26)">Home Cinema</text>
    <path fill="var(--blue)" d="M78,592 Q110,578 190,576 L372,582 L372,616 L78,616 Z"/>
    <path fill="url(#limeSweep)" d="M80,596 Q112,584 190,582 L372,588 L372,614 L80,614 Z"/>
    <text class="contact" x="100" y="608" font-size="11">(m)0412 557 163</text>
    <text class="contact" x="228" y="608" font-size="11">(e)sales@vorplex.com.au</text>
    <rect class="trim-dark" x="196" y="610" width="16" height="36" rx="8"/>
    <text class="licence" x="88" y="670" font-size="14">REC No: 48302</text>
    <text class="brand-name" x="220" y="668" font-size="44" textLength="135" lengthAdjust="spacingAndGlyphs">Vorplex</text>
    <text class="brand-tag" x="238" y="678" font-size="5" textLength="76" lengthAdjust="spacingAndGlyphs">ELECTRICAL, SECURITY, AV</text>
    <rect class="trim-dark" x="90" y="682" width="68" height="8" rx="3"/>
    <rect class="trim-dark" x="292" y="682" width="64" height="8" rx="3"/>
    <path class="trim-dark" d="M148,692 L182,692 L166,704 Z"/>
    <rect fill="var(--plate-yellow)" x="104" y="708" width="98" height="20"/>
    <path fill="var(--blue)" d="M226,740 Q260,716 372,718 L372,740 Z"/>
    <path fill="url(#limeSweep)" d="M232,736 Q266,714 372,716 L372,732 Q300,730 232,736 Z"/>
    <rect class="trim-dark" x="60" y="740" width="330" height="16" rx="3"/>
    <rect class="tail-light" x="90" y="746" width="16" height="8"/>
    <rect class="tail-light" x="342" y="746" width="16" height="8"/>
  </g>
</svg>
</body>
</html>
```